Vertical flyer design to guide people to my shop

We need a vertical flyer design for a tailor shop, Marlow Stitchworks. Our shop is on the 3/F, and we need this flyer/poster to placed on the G/F street level to guide people to take the lifts upstairs. Basically to tell people that, "We are here on 3/F!"

Dimensions ratio: 80 (wide) x200 (tall)

You may use the photos and graphics from the webpages below.
http://www.marlowstitchworks.net/en/marlow-stitchworks-hong-kong-tailors-tailor-shop/

https://www.cloth-q.com/tailor/marlow-stitchworks

```html
<!DOCTYPE html>
<html lang="en">
<head>
<meta charset="utf-8">
<title>Marlow Stitchworks – We Are Here On 3/F</title>
<link rel="stylesheet" href="https://fonts.googleapis.com/css2?family=Cabin:wght@400;500;600;700&display=swap">
<style>
  :root {
    --backdrop: #ebebeb;
    --banner-white: #ffffff;
    --brand-blue: #1a73e8;
    --ink-dark: #2b2b2b;
    --ink-grey: #3d3d3d;
    --frame-grey: #cfcfcf;
  }
  * { margin: 0; padding: 0; box-sizing: border-box; }
  html, body {
    width: 1200px;
    height: 1200px;
    overflow: hidden;
    background: var(--backdrop);
  }
  .stage {
    width: 1200px;
    height: 1200px;
    display: flex;
    align-items: center;
    justify-content: center;
  }
  .rollup-banner {
    width: 440px;
    height: 1100px;
    display: block;
    box-shadow: 0 6px 24px rgba(0,0,0,0.12);
    font-family: "Cabin", sans-serif;
  }
  .headline-top { fill: var(--brand-blue); font-weight: 500; font-size: 40px; letter-spacing: -0.5px; }
  .headline-floor { fill: var(--banner-white); font-weight: 400; font-size: 80px; letter-spacing: -1px; }
  .call-label { fill: var(--brand-blue); font-weight: 700; font-size: 44px; }
  .call-number { fill: var(--ink-grey); font-weight: 600; font-size: 33px; }
  .web-address { fill: var(--banner-white); font-weight: 500; font-size: 17px; }
</style>
</head>
<body>
<main class="stage">
  <svg class="rollup-banner" viewBox="0 0 400 1000" xmlns="http://www.w3.org/2000/svg">
    <defs>
      <linearGradient id="tone-houndstooth" x1="0" y1="0" x2="0" y2="1">
        <stop offset="0" stop-color="#cfcac5"/>
        <stop offset="0.45" stop-color="#b3aca6"/>
        <stop offset="0.75" stop-color="#6f6b68"/>
        <stop offset="1" stop-color="#2a2c33"/>
      </linearGradient>
      <linearGradient id="tone-overcoat" x1="0" y1="0" x2="0" y2="1">
        <stop offset="0" stop-color="#d2ccc6"/>
        <stop offset="0.3" stop-color="#a8958a"/>
        <stop offset="0.6" stop-color="#3e2f29"/>
        <stop offset="1" stop-color="#2c2220"/>
      </linearGradient>
      <linearGradient id="tone-blazer" x1="0" y1="0" x2="0" y2="1">
        <stop offset="0" stop-color="#cdc8c3"/>
        <stop offset="0.45" stop-color="#b59a88"/>
        <stop offset="0.75" stop-color="#3a4a5a"/>
        <stop offset="1" stop-color="#26333f"/>
      </linearGradient>
      <linearGradient id="suit-tone" x1="0" y1="0" x2="0" y2="1">
        <stop offset="0" stop-color="#8a7a6c"/>
        <stop offset="1" stop-color="#4f4036"/>
      </linearGradient>
      <linearGradient id="jacket-tone" x1="0" y1="0" x2="0" y2="1">
        <stop offset="0" stop-color="#3f4a56"/>
        <stop offset="1" stop-color="#a08a76"/>
      </linearGradient>
      <linearGradient id="panel-dark" x1="0" y1="0" x2="1" y2="1">
        <stop offset="0" stop-color="#1f1f1f"/>
        <stop offset="1" stop-color="#4a4a4a"/>
      </linearGradient>
      <linearGradient id="soft-fade" x1="0" y1="0" x2="0" y2="1">
        <stop offset="0" stop-color="#e4e4e4"/>
        <stop offset="1" stop-color="#ffffff"/>
      </linearGradient>
    </defs>

    <rect class="banner-base" x="0" y="0" width="400" height="1000" fill="url(#soft-fade)"/>

    <g class="collage">
      <polygon role="img" aria-label="Photo: model in houndstooth jacket and black turtleneck"
               points="0,0 222,0 190,236 0,150" fill="url(#tone-houndstooth)"/>
      <polygon role="img" aria-label="Photo: model in dark brown overcoat lifting a hat"
               points="232,0 400,0 400,290 324,322 196,255" fill="url(#tone-overcoat)"/>
      <polygon role="img" aria-label="Photo: model in navy blazer and burgundy shirt"
               points="0,160 318,328 0,450" fill="url(#tone-blazer)"/>
      <line x1="226" y1="0" x2="192" y2="248" stroke="#1a73e8" stroke-width="4"/>
      <line x1="0" y1="155" x2="322" y2="325" stroke="#1a73e8" stroke-width="4"/>
      <polygon class="accent-band" points="0,452 400,292 400,325 0,465" fill="#1a73e8"/>
      <polygon class="accent-shadow" points="140,420 400,325 400,338 190,410" fill="#2a2a2a"/>
    </g>

    <g class="floor-panel">
      <rect x="38" y="472" width="328" height="176" fill="url(#panel-dark)"/>
      <polygon points="38,656 366,644 366,650 38,664" fill="#1a73e8"/>
      <text class="headline-top" x="202" y="522" text-anchor="middle">WE ARE HERE</text>
      <text class="headline-floor" x="202" y="616" text-anchor="middle">ON 3/F</text>
    </g>

    <text class="call-label" x="202" y="728" text-anchor="middle">CALL US AT</text>
    <text class="call-number" x="202" y="766" text-anchor="middle">(852) 2481 5096</text>

    <polygon class="footer-band" points="0,905 400,818 400,1000 0,1000" fill="#1a73e8"/>
    <polygon class="footer-shadow" points="0,880 170,842 170,860 0,905" fill="#2b2b2b"/>

    <g class="hex-frame">
      <polygon points="115,785 183,824 183,902 115,941 47,902 47,824" fill="#d0d0d0"/>
      <polygon role="img" aria-label="Photo: model in brown three-piece suit"
               points="115,797 172,830 172,896 115,929 58,896 58,830" fill="url(#suit-tone)"/>
    </g>
    <g class="hex-frame">
      <polygon points="282,772 350,811 350,889 282,928 214,889 214,811" fill="#d0d0d0"/>
      <polygon role="img" aria-label="Photo: tan tweed jacket on a tailor's mannequin"
               points="282,784 339,817 339,883 282,916 225,883 225,817" fill="url(#jacket-tone)"/>
    </g>

    <text class="web-address" x="202" y="972" text-anchor="middle">www.marlowstitchworks.net</text>
  </svg>
</main>
</body>
</html>
```